Menu Design

We want to refresh the feel and look of the menu
but we need to keep the same size and contents. The new design should be modern

Target Market(s)

Onboard Passengers

Industry/Entity Type

Airline

Font styles to use
Sans Serif

Colors

Designer to choose colors to be used in the design.

Requirements
Must have
• Same document size and folding and same contents in PDF

```html
<!DOCTYPE html>
<html lang="en">
<head>
<meta charset="utf-8">
<title>Beverage Menu</title>
<link rel="stylesheet" href="https://fonts.googleapis.com/css2?family=Montserrat:wght@400;600;700&family=Tajawal:wght@500;700&display=swap">
<style>
  :root {
    --backdrop: #d8d3cb;
    --paper: #e3e4e6;
    --teal: #1d7a8e;
    --teal-deep: #15647a;
    --teal-light: #7fc3d2;
    --teal-pale: #a9d8e2;
    --ink: #1f3550;
    --ink-soft: #3d5570;
    --white: #ffffff;
  }
  * { box-sizing: border-box; margin: 0; padding: 0; }
  html, body { width: 1200px; height: 1200px; overflow: hidden; }
  body {
    background: var(--backdrop);
    font-family: "Montserrat", sans-serif;
    color: var(--ink);
  }
  .menu-sheet {
    position: absolute;
    left: 190px; top: 30px;
    width: 820px; height: 1140px;
    background: var(--paper);
    box-shadow: 0 6px 24px rgba(0,0,0,.18);
    overflow: hidden;
  }
  .abs { position: absolute; }

  /* tabs */
  .tab-light { background: var(--teal-light); border-radius: 0 22px 22px 0; }
  .tab-pale { background: var(--teal-pale); border-radius: 22px 0 0 22px; }
  .tab-teal {
    background: linear-gradient(90deg, var(--teal-deep), var(--teal));
    color: var(--white);
  }

  /* header */
  .header-band { left: 0; top: 34px; width: 420px; height: 136px; border-radius: 0 26px 26px 0; display: flex; flex-direction: column; justify-content: center; padding-left: 150px; }
  .header-ar { font-family: "Tajawal", sans-serif; font-weight: 700; font-size: 46px; line-height: 1; direction: rtl; text-align: left; }
  .header-en { font-weight: 600; font-size: 38px; letter-spacing: 5px; line-height: 1.2; }

  /* item text */
  .item { text-align: left; z-index: 2; }
  .item-ar { font-family: "Tajawal", sans-serif; font-weight: 700; font-size: 18px; direction: rtl; text-align: left; display: block; color: var(--ink); white-space: nowrap; }
  .item-en { font-weight: 700; font-size: 15px; color: var(--ink); white-space: nowrap; }
  .item-list { font-weight: 400; font-size: 14px; color: var(--ink-soft); line-height: 1.35; }

  /* price tags */
  .price { display: flex; flex-direction: column; justify-content: center; padding: 0 20px; }
  .price-main { font-weight: 600; font-size: 17px; white-space: nowrap; }
  .price-main b { font-size: 34px; font-weight: 700; letter-spacing: 1px; }
  .price-each { font-size: 14px; font-weight: 600; margin-top: -6px; text-align: right; }
  .price-left { border-radius: 0 20px 20px 0; }
  .price-right { border-radius: 20px 0 0 20px; }

  /* product imagery areas */
  .product { border-radius: 14px; z-index: 1; }
  .product-cup { background: radial-gradient(circle at 50% 40%, #f2efe9, #c9c3bb); }
  .product-cans { background: linear-gradient(90deg, #c8c8ca, #3b7fc0 30%, #3b9a3a 55%, #c8242c 85%); opacity: .85; }
  .product-can { background: linear-gradient(90deg, #2a4f9c, #c9cdd6, #2a4f9c); }
  .product-bottle { background: linear-gradient(180deg, #d6ebf5, #8ec3de); }
</style>
</head>
<body>
<main class="menu-sheet">

  <!-- header -->
  <div class="abs tab-light" style="left:380px; top:20px; width:150px; height:120px;"></div>
  <div class="abs tab-light" style="left:340px; top:34px; width:140px; height:136px; background:var(--teal-pale);"></div>
  <header class="abs tab-teal header-band">
    <span class="header-ar">المشروبات</span>
    <span class="header-en">BEVERAGE</span>
  </header>

  <!-- hot & soft drinks -->
  <section class="abs item" style="left:440px; top:196px; width:240px;">
    <span class="item-ar">كريما كابتشينو</span>
    <p class="item-en">Crema Cappuccino</p>
  </section>
  <section class="abs item" style="left:440px; top:268px; width:240px;">
    <span class="item-ar">مشروبات غازية متنوعة</span>
    <p class="item-en">Soft drinks</p>
    <p class="item-list">Cola Zero, Peak Citrus,<br>Lime Fizz, Classic Cola</p>
  </section>

  <div class="abs product product-cup" role="img" aria-label="Cup of cappuccino with sachet" style="left:40px; top:220px; width:130px; height:150px;"></div>
  <div class="abs product product-cans" role="img" aria-label="Row of assorted soft drink cans" style="left:130px; top:350px; width:300px; height:210px;"></div>

  <!-- price 0.700 -->
  <div class="abs tab-pale" style="left:510px; top:510px; width:170px; height:64px;"></div>
  <div class="abs tab-pale" style="left:560px; top:500px; width:140px; height:64px; background:var(--teal-light);"></div>
  <div class="abs tab-teal price price-right" style="left:630px; top:484px; width:190px; height:72px;">
    <span class="price-main">OMR <b>0.700</b></span>
    <span class="price-each">Each</span>
  </div>

  <!-- energy drink & water -->
  <section class="abs item" style="left:440px; top:740px; width:200px;">
    <span class="item-ar">مشروب الطاقة - فولت</span>
    <p class="item-en">Volt Energy Drink</p>
  </section>
  <section class="abs item" style="left:440px; top:860px; width:200px;">
    <span class="item-ar">مياه معدنية</span>
    <p class="item-en">Mineral Water</p>
  </section>

  <div class="abs product product-can" role="img" aria-label="Slim energy drink can" style="left:250px; top:700px; width:80px; height:210px;"></div>
  <div class="abs product product-bottle" role="img" aria-label="Bottle of mineral water with bubbles" style="left:670px; top:720px; width:120px; height:220px;"></div>

  <!-- price 2.100 -->
  <div class="abs tab-light" style="left:140px; top:770px; width:110px; height:64px; background:var(--teal-pale);"></div>
  <div class="abs tab-light" style="left:120px; top:790px; width:110px; height:64px;"></div>
  <div class="abs tab-teal price price-left" style="left:0; top:798px; width:170px; height:72px;">
    <span class="price-main">OMR <b>2.100</b></span>
    <span class="price-each">Each</span>
  </div>

  <!-- price 0.500 -->
  <div class="abs tab-pale" style="left:520px; top:1060px; width:170px; height:64px;"></div>
  <div class="abs tab-pale" style="left:560px; top:1040px; width:140px; height:64px; background:var(--teal-light);"></div>
  <div class="abs tab-teal price price-right" style="left:630px; top:1020px; width:190px; height:72px;">
    <span class="price-main">OMR <b>0.500</b></span>
    <span class="price-each">Each</span>
  </div>

</main>
</body>
</html>
```